Lumo Cafe Coffee Beans Bag Design

We are an Ethiopian owned coffee shop in D.C looking to create an eye catching design to put onto bag of beans to sell. Our brand is surrounding innovating and modernizing Ethiopian coffee with a chic retro theme. Our bags should highlight the origin of the beans, sustainability as well as general info about the specific beans or at least a space for it. Uploaded is our current logo and we would love if the colors incorporated on the bag play well with our brand color, that beautiful emerald/blue-green. I have also uploaded some other coffee brands coffee bags as inspiration for the direction we would like to go with regarding the design and bag type. Lastly, I have also uploaded the template that the bag manufacturers have asked us to design the bags with these dimensions in mind, so designing the bags within the bounds of this bag would be required. Thank you!

Target Market(s)

Coffee market

Industry/Entity Type

Coffee/Cafe & Restaurant Merchandize

Font styles to use
Other font styles liked:
• Rockwell, Bodoni, Gabriela Stencil

Colors
0054AA
0677BA
7BADD7
CADEEF
E8F1F8
0094D4
00A9DD
6FCCEA
C7EBF8
E9F6FB
00AB8E
00BBA5
67D7C9
C6EFE9
E9F9F6

Requirements
Must have
• Must incorporate a logo and include a space to include information about the beans
Nice to have
• A 70s vintage/funky design feeling to the bag. We would love if the bag design felt novel or interesting to catch customers attention and for the design to not be one that blends in with other coffee bags. This is something that should stand out and be fun.
Should not have
• The bag design shouldn't be a cut and dry design. Whether in the form of a simple sticker or slapping the logo onto the bag itself, the design should be novel and shouldn't look straight forward and boring.

```html
<!DOCTYPE html>
<html lang="en">
<head>
<meta charset="utf-8">
<title>Lumo Cafe – Coffee Bag Label</title>
<link href="https://fonts.googleapis.com/css2?family=Gelasio:wght@400&family=Josefin+Sans:wght@300;400&family=Tinos&display=swap" rel="stylesheet">
<style>
  :root {
    --stage: #ecebe8;
    --ivory: #efeae0;
    --emerald: #12382c;
    --white: #ffffff;
    --ink: #12382c;
  }
  * { margin: 0; padding: 0; box-sizing: border-box; }
  html, body { width: 1200px; height: 656px; overflow: hidden; }
  body { background: var(--stage); position: relative; }

  .label {
    position: absolute; left: 388px; top: 28px;
    width: 424px; height: 600px;
  }
  .label-border {
    position: absolute; inset: 0;
    background: var(--ivory);
  }
  .label-panel {
    position: absolute; left: 30px; top: 30px;
    width: 364px; height: 540px;
  }
  .panel-content {
    position: absolute; left: 30px; top: 30px;
    width: 364px; height: 540px;
    color: var(--white);
    text-align: center;
  }

  .brand-name {
    position: absolute; left: 0; right: 0; top: 64px;
    font-family: "Gelasio", serif;
    font-weight: 400;
    font-size: 66px;
    line-height: 58px;
    color: var(--white);
    letter-spacing: -1px;
  }

  .rule {
    position: absolute; left: 0; right: 0;
    height: 1.5px; background: var(--white);
  }
  .rule-top { top: 250px; }
  .rule-band-top { top: 413px; }
  .rule-band-bottom { top: 449px; }
  .band-divider {
    position: absolute; left: 173px; top: 413px;
    width: 1.5px; height: 37px; background: var(--white);
  }

  .premium-tag {
    position: absolute; left: 125px; top: 239px;
    width: 111px; height: 21px;
    background: var(--white);
    color: var(--ink);
    font-family: "Josefin Sans", sans-serif;
    font-weight: 400;
    font-size: 11px;
    letter-spacing: 2.4px;
    line-height: 23px;
    clip-path: polygon(0 0, 100% 0, 94% 50%, 100% 100%, 0 100%, 6% 50%);
  }

  .origin-kicker {
    position: absolute; left: 0; right: 0; top: 280px;
    font-family: "Josefin Sans", sans-serif;
    font-weight: 300;
    font-size: 12px;
    letter-spacing: 5px;
  }
  .origin-title {
    position: absolute; left: 0; right: 0; top: 305px;
    font-family: "Gelasio", serif;
    font-size: 35px;
    line-height: 42px;
  }

  .bean-note {
    position: absolute; top: 413px; height: 37px;
    font-family: "Josefin Sans", sans-serif;
    font-weight: 300;
    font-size: 15px;
    letter-spacing: 3.4px;
    line-height: 40px;
  }
  .bean-note-roasted { left: 0; width: 173px; }
  .bean-note-dried { left: 175px; width: 189px; }

  .bean-info {
    position: absolute; left: 30px; right: 30px; top: 464px;
    font-family: "Tinos", serif;
    font-size: 8.5px;
    line-height: 10px;
  }
  .net-weight {
    position: absolute; left: 0; right: 0; top: 504px;
    font-family: "Tinos", serif;
    font-size: 11px;
  }
</style>
</head>
<body>
  <main class="label">
    <div class="label-border" role="img" aria-label="Ivory damask pattern border"></div>

    <svg class="label-panel" width="364" height="540" viewBox="0 0 364 540" role="img" aria-label="Deep emerald panel with tone-on-tone damask pattern">
      <path fill="var(--emerald)" d="M33,0 H331 A33,33 0 0 0 364,33 V507 A33,33 0 0 0 331,540 H33 A33,33 0 0 0 0,507 V33 A33,33 0 0 0 33,0 Z"/>
    </svg>

    <div class="panel-content">
      <h1 class="brand-name">lumo<br>café</h1>

      <div class="rule rule-top"></div>
      <div class="premium-tag">PREMIUM</div>

      <p class="origin-kicker">FLAVORS FROM</p>
      <h2 class="origin-title">The Ethiopian<br>Highlands</h2>

      <div class="rule rule-band-top"></div>
      <div class="band-divider"></div>
      <div class="rule rule-band-bottom"></div>
      <p class="bean-note bean-note-roasted">ROASTED</p>
      <p class="bean-note bean-note-dried">SUN DRIED</p>

      <p class="bean-info">It is a long established fact that a reader will be distracted by the readable content of a page when looking at its layout.</p>
      <p class="net-weight">NET WEIGHT 250G</p>
    </div>
  </main>
</body>
</html>
```